Flyer for IT Support Company

We need a 1 sided A5 flyer to promote our services and support packages to local businesses, I have attached the sort of content and layout we are looking for but happy for you to be creative with backgrounds and colors. It needs to look modern and professional but catch the eye ;-)
The strap-line on the logo needs to be changed to to 'Your Local IT Company'

It Company

```html
<!DOCTYPE html>
<html lang="en">
<head>
<meta charset="utf-8">
<title>Corvanet – Affordable IT Support Packages</title>
<link href="https://fonts.googleapis.com/css2?family=Lato:wght@400;700;900&family=Squada+One&display=swap" rel="stylesheet">
<style>
  :root{
    --green:#8ba524;
    --green-dark:#6c8719;
    --pink:#d9157f;
    --ink:#1f1f1f;
    --panel:#efefef;
    --white:#ffffff;
  }
  *{box-sizing:border-box;margin:0;padding:0}
  html,body{width:904px;height:1200px;overflow:hidden;background:var(--white)}
  body{font-family:"Lato",sans-serif;color:var(--ink);position:relative}

  .flyer{position:absolute;inset:0;background:var(--white);overflow:hidden}

  .header-art{position:absolute;left:0;top:0;width:904px;height:190px}
  .brand{position:absolute;left:96px;top:38px;color:var(--white)}
  .brand-name{display:flex;align-items:center;gap:12px;font-weight:900;font-size:64px;line-height:1;letter-spacing:-1px}
  .brand-dot{width:40px;height:40px;border-radius:50%;background:var(--white)}
  .brand-tagline{margin-top:6px;margin-left:54px;font-size:14px;letter-spacing:2.5px;color:#e9f1cf}

  .badge{position:absolute;left:560px;top:12px;width:280px;height:280px}
  .badge-text{position:absolute;left:560px;top:12px;width:280px;height:280px;display:flex;align-items:center;justify-content:center;text-align:center;color:var(--white);font-weight:900;font-size:27px;line-height:1.08;transform:rotate(15deg)}

  .intro{position:absolute;left:102px;top:182px}
  .intro-title{color:var(--green);font-weight:900;font-size:30px}
  .intro-sub{margin-top:6px;font-size:29px;line-height:1.25;color:#222}

  .packages{position:absolute;left:14px;top:306px;width:826px;height:612px;background:var(--panel);box-shadow:0 3px 10px rgba(0,0,0,.35);overflow:hidden}
  .grid-row{display:grid;grid-template-columns:260px repeat(4,1fr);align-items:center}
  .packages-head{background:linear-gradient(180deg,var(--green),var(--green-dark));color:var(--white);font-weight:700;font-size:21px;padding:10px 0;height:102px;display:flex;flex-direction:column;justify-content:center}
  .packages-head .grid-row{height:27px}
  .packages-head .cell{text-align:center}
  .section-band{position:relative;height:34px}
  .section-band::before{content:"";position:absolute;left:0;right:0;top:14px;height:6px;background:var(--pink)}
  .section-label{position:absolute;left:50%;top:4px;transform:translateX(-50%);background:var(--pink);color:#2a0a1a;font-size:17px;line-height:20px;padding:3px 16px;border-radius:14px;white-space:nowrap}
  .rows{padding:4px 0 8px}
  .rows .grid-row{height:20px;font-size:16px;line-height:20px}
  .rows .label{padding-left:14px}
  .rows .cell{text-align:center}
  .tick{color:var(--pink);font-size:13px}

  .features{position:absolute;left:0;top:938px;width:904px;height:130px}
  .feature{position:absolute;top:0;width:128px;height:128px;border-radius:50%;background:var(--pink);display:flex;align-items:center;justify-content:center;text-align:center;color:var(--white);font-family:"Squada One",sans-serif;font-size:19px;line-height:1.25;text-transform:uppercase}
  .feature::after{content:"";position:absolute;inset:8px;border:2px dashed var(--white);border-radius:50%}

  .contact{position:absolute;left:12px;top:1074px;width:826px;height:104px;border-radius:14px;background:linear-gradient(180deg,var(--green),var(--green-dark));text-align:center}
  .contact-pitch{padding-top:8px;font-family:"Squada One",sans-serif;font-size:24px;line-height:1.2;color:#1d2a06;text-transform:uppercase}
  .contact-lines{display:flex;justify-content:space-between;align-items:center;padding:8px 18px 0 14px;color:var(--white);font-weight:700;font-size:24px}
  .contact-item{display:flex;align-items:center;gap:6px}
  .contact-item svg{width:16px;height:16px}
</style>
</head>
<body>
<main class="flyer">

  <svg class="header-art" viewBox="0 0 904 190" aria-hidden="true">
    <path d="M0 0H904V100C700 150 360 150 0 120Z" fill="var(--green)"/>
    <path d="M0 130C300 165 660 150 904 118V134C660 170 300 185 0 152Z" fill="var(--pink)"/>
  </svg>

  <div class="brand">
    <div class="brand-name"><span class="brand-dot"></span>corvanet</div>
    <div class="brand-tagline">Your Local IT Company</div>
  </div>

  <svg class="badge" viewBox="0 0 280 280" aria-hidden="true">
    <circle cx="140" cy="140" r="128" fill="none" stroke="var(--white)" stroke-width="10"/>
    <circle cx="140" cy="140" r="118" fill="var(--pink)"/>
    <circle cx="140" cy="140" r="120" fill="none" stroke="var(--pink)" stroke-width="10" stroke-dasharray="7 7"/>
  </svg>
  <div class="badge-text">IT support from<br>$10pm- from a<br>trusted provider<br>based in<br>Wrexham</div>

  <section class="intro">
    <h1 class="intro-title">Affordable IT Support Packages</h1>
    <p class="intro-sub">Peace of mind for your business at<br>competitive prices</p>
  </section>

  <section class="packages">
    <div class="packages-head">
      <div class="grid-row"><div class="cell">IT Support Packages</div><div class="cell">Remote</div><div class="cell">Plus</div><div class="cell">Pro</div><div class="cell">Unlimited</div></div>
      <div class="grid-row"><div class="cell">Per Server</div><div class="cell">£45pm</div><div class="cell">£85pm</div><div class="cell">£85pm</div><div class="cell">£85pm</div></div>
      <div class="grid-row"><div class="cell">Per Computers</div><div class="cell">£10pm</div><div class="cell">£10pm</div><div class="cell">£13pm</div><div class="cell">£15pm</div></div>
    </div>

    <div class="section-band"><span class="section-label">SUPPORT SERVICE</span></div>
    <div class="rows">
      <div class="grid-row"><span class="label">Server support</span><span class="cell tick">✔</span><span class="cell tick">✔</span><span class="cell tick">✔</span><span class="cell tick">✔</span></div>
      <div class="grid-row"><span class="label">PC/device support</span><span class="cell tick">✔</span><span class="cell tick">✔</span><span class="cell tick">✔</span><span class="cell tick">✔</span></div>
    </div>

    <div class="section-band"><span class="section-label">SERVER/NETWORK CALLOUT</span></div>
    <div class="rows">
      <div class="grid-row"><span class="label">Remote support</span><span class="cell tick">✔</span><span class="cell tick">✔</span><span class="cell tick">✔</span><span class="cell tick">✔</span></div>
      <div class="grid-row"><span class="label">Onsite callout (4hr response)</span><span class="cell">£40</span><span class="cell tick">✔</span><span class="cell tick">✔</span><span class="cell tick">✔</span></div>
      <div class="grid-row"><span class="label">Hourly rate onsite</span><span class="cell">£25ph</span><span class="cell">Included</span><span class="cell">Included</span><span class="cell">Included</span></div>
    </div>

    <div class="section-band"><span class="section-label">PROTECTION/SECURITY</span></div>
    <div class="rows">
      <div class="grid-row"><span class="label">Core anti-virus (per PC)</span><span class="cell">£2</span><span class="cell">£2</span><span class="cell">£2</span><span class="cell tick">✔</span></div>
      <div class="grid-row"><span class="label">Core content filter (per PC)</span><span class="cell">£1.30</span><span class="cell">£1.30</span><span class="cell">£1.30</span><span class="cell tick">✔</span></div>
      <div class="grid-row"><span class="label">Remote back-up (per unit, 5GB)</span><span class="cell">£1.50</span><span class="cell">£1.50</span><span class="cell">£1.50</span><span class="cell tick">✔</span></div>
    </div>

    <div class="section-band"><span class="section-label">MONITORING</span></div>
    <div class="rows">
      <div class="grid-row"><span class="label">Daily back-up checks</span><span class="cell tick">✔</span><span class="cell tick">✔</span><span class="cell tick">✔</span><span class="cell tick">✔</span></div>
      <div class="grid-row"><span class="label">24/7 monitoring</span><span class="cell tick">✔</span><span class="cell tick">✔</span><span class="cell tick">✔</span><span class="cell tick">✔</span></div>
    </div>

    <div class="section-band"><span class="section-label">MAINTENANCE</span></div>
    <div class="rows">
      <div class="grid-row"><span class="label">Patch management</span><span class="cell tick">✔</span><span class="cell tick">✔</span><span class="cell tick">✔</span><span class="cell tick">✔</span></div>
      <div class="grid-row"><span class="label">Software updates</span><span class="cell tick">✔</span><span class="cell tick">✔</span><span class="cell tick">✔</span><span class="cell tick">✔</span></div>
      <div class="grid-row"><span class="label">Security updates</span><span class="cell tick">✔</span><span class="cell tick">✔</span><span class="cell tick">✔</span><span class="cell tick">✔</span></div>
    </div>
  </section>

  <section class="features">
    <div class="feature" style="left:31px">Affordable,<br>local<br>service</div>
    <div class="feature" style="left:195px">4 hour<br>callout</div>
    <div class="feature" style="left:367px">Remote<br>support</div>
    <div class="feature" style="left:535px">24/7<br>monitoring</div>
    <div class="feature" style="left:699px">Server/PC<br>builds from<br>£250</div>
  </section>

  <footer class="contact">
    <p class="contact-pitch">Protect your business and keep downtime costs at bay<br>Call, email or live chat with us on our website today!</p>
    <div class="contact-lines">
      <span class="contact-item">
        <svg viewBox="0 0 16 16" aria-hidden="true"><rect x="0" y="0" width="16" height="16" rx="3" fill="var(--pink)"/><path d="M5 3.5l2 2-1 1.2c.6 1.3 1.6 2.3 2.8 2.8l1.2-1 2 2-1.3 1.5C7.4 11.7 4.3 8.6 3.5 5.3Z" fill="var(--white)"/></svg>
        01632 960 482</span>
      <span class="contact-item">
        <svg viewBox="0 0 16 16" aria-hidden="true"><rect x="1" y="3" width="14" height="10" fill="none" stroke="var(--pink)" stroke-width="1.5"/><path d="M1 3l7 6 7-6" fill="none" stroke="var(--pink)" stroke-width="1.5"/></svg>
        info@corvanet.co.uk</span>
      <span class="contact-item">
        <svg viewBox="0 0 16 16" aria-hidden="true"><circle cx="8" cy="8" r="7" fill="none" stroke="var(--pink)" stroke-width="1.5"/><ellipse cx="8" cy="8" rx="3" ry="7" fill="none" stroke="var(--pink)" stroke-width="1.2"/><path d="M1 8h14" stroke="var(--pink)" stroke-width="1.2"/></svg>
        www.corvanet.co.uk</span>
    </div>
  </footer>

</main>
</body>
</html>
```